Mobile Repair Service on location needs a Web Design

We are starting a new mobile device repair service called Gadget Haven and our website needs a design!

Hello Designers!
First, we'd like to make clear this is more than a simple web design contest, we want the designers to create an idea. We want someone who can create the whole theme of the service's we provide. We want someone that can help design our visual branding, help us communicate a sentiment. And we are willing to pay for that.

Who are we?
Our company is based in Rotterdam, the Netherlands. We provide different services for all kinds of electronic devices. The kind of services we provide are, among other things, installations of hardware and software and the repair of broken or malfunctioning devices.
We are starting a new service that offers mobile device repairs on location, be it at the home of our customers, their office, or any other place. Just give us the address and we will come to you for the repair job. This is also our main USP. We have multiple skilled engineers who drive trough the country on a daily basis and can be on location within a working day. Repair is done immediately onsite while the customer waits. At this stage we will start with the smartphone product-group within the mobile devices. In a second phase we might also add tablets.
People don't want to be without their phone for weeks because of some parts that needed to be ordered by a repair center they had to sent their phone to. We offer a fully functional mobile repair center in the form of specially customized vans. These vans have all the tools and utilities needed by our engineers to safely repair your mobile device. Your phone is being repaired directly in front of you, the next business-day, on a location you desire.

For this new service we are creating a website called Gadget Haven. The website needs a story and matching design and this is where you come in. We are not looking for a simple template design we can get from any place. We need a story. We want you to create an idea, build a unique theme or vision that helps sell the product/service. This goes beyond the design of the website. We need the whole package, the design you are creating needs to have returning elements like icons, color use, images, maybe even characters etc. You name it! There needs to be a common thread in the design so we can reuse elements in, for example, the email templates, the work order or receipt we give to our customers (we may contact the winner of the contest to design these for us as well!).

The name 'Gadget Haven' is chosen. Haven (short for rehabilitate) has a bold and playful tone to it and the design needs to reflect the name. So we're looking for a somewhat playful and cheeky design. Definitely not too serious and definitely modern. We already got a logo that we love and that fit's this description (see attached design documents for the logo). It's bold, powerful and fun. Our web design needs to reflect this as well and has to fit in with our logo.
We would really like it if the design somehow incorporates elements that highlight our unique selling points (repairs on location, we come to you etc.). We would really like some form of story telling in the design. Think clumsy people breaking their phones. Teenagers in tears because they have no access to their friends. People nowadays have the need to always be 'connected'. What happens when your phone is broken or malfunctioning? We're handling tech, we are nerds and a little bit weird, but we're professionals and here to help you with your problem. The sentiment Wire Troop tries to communicate is something we really like. We're looking for fresh idea's, anything goes!

In an overview all Unique Selling Points of the Gadget haven service:
- Professional service on location. Don’t ship to us we will come to you!
- Clear pricing upfront. No hidden cost.
- Next business-day repair.
- Backed by a professional call center open 12 hours a day and open on a Saturday as well
- Backed by a professional repair center with more then 12 years of experience
- Repair is done by certified engineers
- 1 year warranty on the repair

The process:
The main function of our website will be for customers to make a repair request. A customer will visit our website and can make a repair request immediately by going through a 'request-order-flow'. In this flow he or she will need to fill in some forms and can select wich type/model/brand of mobile device he or she has and what parts need to be repaired. After a request is placed we will call the customer back (within an hour) for a short intake and to set a date/time and location. Our engineer will meet the customer at the specified location and will repair the device onsite in one of our mobile repair centers, which is a specialized van equipped with all the tools needed for device restorations.
So in short the steps are:
- Choose your device and repair job
- Place the order
- Get a callback within the hour
- Set date and location
- We will come to you.

Website functionality:
Our website is our main form of communication. So the sentiment we want to communicate needs be reflected in the design. We need a main/front page designed (preferably a long scrolling page design) containing:
1. Customers will be able to request a repair job directly on our website. So there will need to be a prominent button/link at the top of our main page that will bring the customer to this 'request-order-flow'. This is the main flow which needs to be full focus on the front page. All other items are secondary.
2. The general information of who we are and what we do, and why the customer should choose us. Preferably in short bullet-point type keywords/sentences with icons or other visual cues. See our unique selling points to get an idea of the information that will be displayed here.
3. There needs to be a section that will explain the process (see above) of a repair request step-by- step, again in brief short key sentences and with (custom) icons.
4. There needs to be a section that explains to the customer he/she can always contact us if they are not sure what the problem is with their device, and for this reason are not sure what repair request they should order.
5. We want to implement some functionality that display customer ratings or customer reviews. So there needs to be room for some kind of widget of plugin we're going to implement which shows these reviews.
6. A 'For business section' where we will explain all the options we provide for corporate clients.
7. Social media links.
8. There needs to be a menu with buttons that leads to the all sections described in the previous points.

For now, we need a design for our front page. In the second phase, when we have picked our winner, we may ask the winner to design the page(s) for our request workflow as well.

EDIT:
Finally, we have a very specific order in mind for the different segments of our website. We would like you to add some more segments that were not in our original brief as well:

1. Top header with order/request button. (should instantly make clear our main USP, we do repairs on location)
2. Our process
3. Our unique selling points / why choose us
4. The kind of repairs we do (broken screens, broken batteries, water damage, broken camera's, no sound etc.)
5. A 'meet our team' section, where we introduce some of our engineers
6. A 'contact us for any questions' section/
7. Testimonials/user reviews
8. A section where we show key performance indicators
9. 'For businesses' sections
10.'Subscribe for newsletter' field
11. Social media buttons

Industry/Entity Type

It Service

Number of Pages Required

1 page

Font styles to use
Sans Serif

Requirements
Must have
• a main/front page, design only
• custom icons/images for banners, adverts online and in print (high res)
Nice to have
• Storytelling in our design.
• Design that fits with our brand new logo.
• Elements like icons to have a flat design.
• Keep in mind that the website will need to be responsive when designing! (Ideally provide an example of the mobile design as well)
• Create a fun and trustworthy feeling.

```html
<!DOCTYPE html>
<html lang="en">
<head>
<meta charset="utf-8">
<title>Gadget Haven – Mobile repair on location</title>
<link rel="stylesheet" href="https://fonts.googleapis.com/css2?family=Oswald:wght@500;600&family=Open+Sans:wght@400;600;700&display=swap">
<style>
:root{
  --orange:#f3702f;
  --orange-deep:#ee6424;
  --lavender:#bdb9e2;
  --lavender-field:#c7c3ea;
  --purple:#8e86c8;
  --purple-line:#7d74c0;
  --navy:#0c1030;
  --ink:#1a1a1a;
  --grey-text:#555;
  --band:#f1f1f1;
  --white:#fff;
  --thin:#e39a74;
}
*{box-sizing:border-box;margin:0;padding:0}
html,body{width:1200px;height:3087px;overflow:hidden}
body{position:relative;background:var(--white);font-family:"Open Sans",Arial,sans-serif;color:var(--ink)}
.abs{position:absolute}

/* hero */
.hero{left:0;top:0;width:1200px;height:580px}
.hero-photo{position:absolute;inset:0;
  background:
    linear-gradient(180deg,rgba(40,46,58,.35) 0%,rgba(40,46,58,.15) 45%,rgba(30,34,44,.45) 100%),
    radial-gradient(ellipse 260px 160px at 330px 190px,#c9ccd2 0%,rgba(201,204,210,0) 100%),
    radial-gradient(ellipse 320px 200px at 760px 300px,#b6a9a6 0%,rgba(182,169,166,0) 100%),
    radial-gradient(ellipse 360px 220px at 1000px 140px,#9ea4ae 0%,rgba(158,164,174,0) 100%),
    radial-gradient(ellipse 420px 200px at 140px 520px,#2c3038 0%,rgba(44,48,56,0) 100%),
    linear-gradient(160deg,#7f8791 0%,#6c737e 40%,#555c67 70%,#454a54 100%)}
.hero-side{left:0;top:580px;width:160px;height:83px;background:linear-gradient(180deg,#3a3e47,#50555e)}
.brand{left:163px;top:24px;display:flex;align-items:center;gap:12px}
.brand-mark{width:60px;height:60px;border-radius:50%;background:var(--orange)}
.brand-text{display:flex;flex-direction:column}
.brand-name{font-weight:700;font-size:24px;line-height:1;color:var(--white);width:110px}
.brand-tag{font-weight:700;font-size:10px;color:var(--white);margin-top:4px}
.main-nav a{position:absolute;top:54px;color:var(--white);text-decoration:none;font-size:13px;white-space:nowrap}
.menu-btn{left:994px;top:38px;width:44px;height:44px;background:var(--orange-deep);display:flex;flex-direction:column;justify-content:center;align-items:center;gap:5px}
.menu-btn span{display:block;width:18px;height:2px;background:var(--white)}
.menu-btn span:last-child{width:12px;margin-left:6px}
.perk{width:190px;text-align:center;color:var(--white);font-size:16px;line-height:1.25}
.perk-ring{width:108px;height:108px;margin:0 auto 8px;border:2px dotted rgba(255,255,255,.85);border-radius:50%;display:flex;align-items:center;justify-content:center}

/* who */
.who-photo{left:160px;top:580px;width:355px;height:435px;
  background:
    radial-gradient(ellipse 110px 150px at 230px 250px,#2a2c30 0%,#3a3c40 60%,rgba(58,60,64,0) 100%),
    radial-gradient(ellipse 170px 120px at 110px 130px,#e2b9a2 0%,rgba(226,185,162,0) 100%),
    linear-gradient(180deg,#fafafa,#f0eeec)}
.who-panel{left:515px;top:580px;width:685px;height:435px;background:var(--orange)}
.who-title{left:586px;top:630px;font-family:"Oswald",Arial,sans-serif;font-weight:600;font-size:46px;color:var(--white)}
.who-copy{left:586px;top:708px;width:565px;color:var(--white);font-size:10.5px;line-height:1.55}
.who-copy p{margin-bottom:10px}
.who-badge{left:992px;top:622px;width:44px;height:44px;border-radius:50%;background:var(--white)}

/* process */
.section-title{font-family:"Oswald",Arial,sans-serif;font-weight:500;font-size:46px;color:var(--ink);text-align:center;width:1200px;left:0}
.title-bar{width:44px;height:5px;background:var(--orange);left:578px}
.thin{background:var(--thin);height:1px}
.thin-v{background:var(--thin);width:1px}
.process-intro{left:230px;top:1194px;width:740px;text-align:center;font-size:10.5px;color:var(--grey-text);line-height:1.7}
.step{width:190px;text-align:center;font-size:14px;line-height:1.3;color:var(--ink)}
.step svg{display:block;margin:0 auto 10px}

/* services */
.services-band{left:0;top:1540px;width:1200px;height:98px;background:var(--band)}
.tile{width:290px;height:278px}
.tile-text{background:var(--orange);color:var(--white);font-size:10px;line-height:1.6}
.tile-text p{margin-bottom:9px}
.tile-text ul{list-style:none}
.tile-text li{margin-bottom:4px}

/* contact */
.contact{left:0;top:2542px;width:1200px;height:479px;
  background:
    radial-gradient(ellipse 300px 200px at 420px 80px,rgba(110,112,118,.55),rgba(110,112,118,0)),
    radial-gradient(ellipse 380px 240px at 1000px 330px,rgba(70,72,78,.6),rgba(70,72,78,0)),
    linear-gradient(180deg,#3b3d42,#23252a 60%,#1b1c20)}
.contact-title{left:0;top:2592px;width:1200px;text-align:center;font-weight:600;font-size:40px;color:var(--white)}
.field{background:var(--lavender-field);color:#554e8e;font-size:12px;padding:12px 18px}
.field b{color:var(--orange);font-weight:400}
.send{left:490px;top:2941px;width:220px;height:49px;background:var(--purple);color:var(--white);font-size:12px;letter-spacing:.5px;display:flex;align-items:center;justify-content:center}

/* footer */
.footer{left:0;top:3021px;width:1200px;height:66px;background:var(--navy);color:var(--white);text-align:center}
.footer nav{padding-top:17px;font-size:11px}
.footer nav a{color:var(--white);text-decoration:none;margin:0 28px}
.footer small{display:block;margin-top:9px;font-size:10px}
</style>
</head>
<body>

<section class="abs hero">
  <div class="hero-photo" role="img" aria-label="Hands holding a smartphone above a laptop keyboard"></div>
  <div class="abs brand"><span class="brand-mark"></span><span class="brand-text"><span class="brand-name">GADGET HAVEN</span><span class="brand-tag">We will come to you!</span></span></div>
  <nav class="main-nav">
    <a href="#" style="left:424px">Home</a>
    <a href="#" style="left:513px">Who are we?</a>
    <a href="#" style="left:647px">Service</a>
    <a href="#" style="left:744px">The process</a>
    <a href="#" style="left:867px">Contact</a>
  </nav>
  <div class="abs menu-btn"><span></span><span></span><span></span></div>

  <div class="abs perk" style="left:230px;top:378px">
    <div class="perk-ring"><svg width="40" height="56" viewBox="0 0 40 56"><text x="20" y="46" text-anchor="middle" font-family="Open Sans,Arial,sans-serif" font-weight="700" font-size="50" fill="#fff">$</text></svg></div>Clear pricing upfront</div>
  <div class="abs perk" style="left:427px;top:378px">
    <div class="perk-ring"><svg width="36" height="58" viewBox="0 0 36 58"><rect x="2" y="2" width="32" height="54" rx="5" fill="none" stroke="#fff" stroke-width="3"/><path d="M10 40 L24 16" stroke="#fff" stroke-width="4" stroke-linecap="round"/></svg></div>Next business<br>-day repair</div>
  <div class="abs perk" style="left:605px;top:378px">
    <div class="perk-ring"><svg width="66" height="66" viewBox="0 0 66 66"><path d="M58 33 A25 25 0 1 1 48 13" fill="none" stroke="#fff" stroke-width="4"/><path d="M44 6 L52 13 L43 19" fill="#fff"/><text x="33" y="33" text-anchor="middle" font-family="Oswald,Arial,sans-serif" font-size="20" fill="#fff">12</text><text x="33" y="48" text-anchor="middle" font-family="Oswald,Arial,sans-serif" font-size="12" fill="#fff">HR</text></svg></div>12 hours a day</div>
  <div class="abs perk" style="left:797px;top:378px">
    <div class="perk-ring"><svg width="60" height="60" viewBox="0 0 60 60"><text x="30" y="38" text-anchor="middle" font-family="Oswald,Arial,sans-serif" font-weight="600" font-size="36" fill="#fff">12</text><text x="30" y="52" text-anchor="middle" font-family="Open Sans,Arial,sans-serif" font-size="11" fill="#fff">years</text></svg></div>12 years of<br>experience</div>
</section>

<div class="abs hero-side" role="img" aria-label="Continuation of the laptop keyboard photo"></div>

<div class="abs who-photo" role="img" aria-label="Hand holding a smartphone with a shattered screen on a white background"></div>
<section class="abs who-panel"></section>
<div class="abs thin-v" style="left:585px;top:580px;height:56px;background:#ffd2bb"></div>
<div class="abs thin" style="left:520px;top:635px;width:66px;background:#ffd2bb"></div>
<h2 class="abs who-title">Who are we?</h2>
<div class="abs who-badge"></div>
<div class="abs who-copy">
  <p>Our company is based in Rotterdam, the Netherlands. We provide different services for all kinds of electronic devices. The kind of services we provide are, among other things, installations of hardware and software and the repair of broken or malfunctioning devices.</p>
  <p>We are starting a new service that offers mobile device repairs on location, be it at the home of our customers, their office, or any other place. Just give us the address and we will come to you for the repair job. This is also our main USP. We have multiple skilled engineers who drive trough the country on a daily basis and can be on location within a working day. Repair is done immediately onsite while the customer waits. At this stage we will start with the smartphone product-group within the mobile devices. In a second phase we might also add tablets.</p>
  <p>People don't want to be without their phone for weeks because of some parts that needed to be ordered by a repair center they had to sent their phone to. We offer a fully functional mobile repair center in the form of specially customized vans. These vans have all the tools and utilities needed by our engineers to safely repair your mobile device. Your phone is being repaired directly in front of you, the next business-day, on a location you desire.</p>
</div>

<div class="abs thin-v" style="left:488px;top:1052px;height:66px"></div>
<div class="abs thin" style="left:420px;top:1108px;width:70px"></div>
<div class="abs thin-v" style="left:712px;top:1125px;height:62px"></div>
<div class="abs thin" style="left:712px;top:1125px;width:60px"></div>
<h2 class="abs section-title" style="top:1082px">The Process:</h2>
<div class="abs title-bar" style="top:1160px"></div>
<p class="abs process-intro">People don't want to be without their phone for weeks because of some parts that needed to be ordered by a repair center they had to sent their phone to. We offer a fully functional mobile repair center in the form of specially customized vans.</p>

<div class="abs step" style="left:138px;top:1262px">
  <svg width="148" height="172" viewBox="0 0 148 172"><path d="M74 2 A72 72 0 0 1 118 131 L74 172 L30 131 A72 72 0 0 1 74 2Z" fill="#bdb9e2"/><circle cx="74" cy="72" r="54" fill="#fff" stroke="#7d74c0" stroke-width="3"/><path d="M52 50 L96 94 M96 50 L52 94" stroke="#111" stroke-width="9" stroke-linecap="round"/></svg>
  Choose your<br>device and repair job</div>
<div class="abs step" style="left:331px;top:1262px">
  <svg width="148" height="172" viewBox="0 0 148 172"><path d="M74 2 A72 72 0 0 1 118 131 L74 172 L30 131 A72 72 0 0 1 74 2Z" fill="#bdb9e2"/><circle cx="74" cy="72" r="54" fill="#fff" stroke="#7d74c0" stroke-width="3"/><path d="M74 102 C60 82 58 74 58 66 A16 16 0 0 1 90 66 C90 74 88 82 74 102Z" fill="#111"/><circle cx="74" cy="66" r="6" fill="#fff"/></svg>
  Place the order</div>
<div class="abs step" style="left:512px;top:1262px">
  <svg width="148" height="172" viewBox="0 0 148 172"><path d="M74 2 A72 72 0 0 1 118 131 L74 172 L30 131 A72 72 0 0 1 74 2Z" fill="#bdb9e2"/><circle cx="74" cy="72" r="54" fill="#fff" stroke="#7d74c0" stroke-width="3"/><rect x="60" y="44" width="30" height="54" rx="5" fill="#111"/><rect x="64" y="50" width="22" height="38" fill="#fff"/></svg>
  Get a callback<br>within the hour</div>
<div class="abs step" style="left:691px;top:1262px">
  <svg width="148" height="172" viewBox="0 0 148 172"><path d="M74 2 A72 72 0 0 1 118 131 L74 172 L30 131 A72 72 0 0 1 74 2Z" fill="#bdb9e2"/><circle cx="74" cy="72" r="54" fill="#fff" stroke="#7d74c0" stroke-width="3"/><rect x="50" y="50" width="46" height="42" rx="3" fill="#111"/><rect x="54" y="62" width="38" height="26" fill="#fff"/><g fill="#111"><rect x="57" y="65" width="6" height="5"/><rect x="67" y="65" width="6" height="5"/><rect x="77" y="65" width="6" height="5"/><rect x="57" y="74" width="6" height="5"/><rect x="67" y="74" width="6" height="5"/></g><circle cx="94" cy="90" r="10" fill="#111" stroke="#fff" stroke-width="2"/></svg>
  Set date and location</div>
<div class="abs step" style="left:870px;top:1262px">
  <svg width="148" height="172" viewBox="0 0 148 172"><path d="M74 2 A72 72 0 0 1 118 131 L74 172 L30 131 A72 72 0 0 1 74 2Z" fill="#bdb9e2"/><circle cx="74" cy="72" r="54" fill="#fff" stroke="#7d74c0" stroke-width="3"/><rect x="44" y="56" width="40" height="28" fill="#111"/><path d="M84 64 H98 L106 74 V84 H84Z" fill="#111"/><circle cx="56" cy="88" r="6" fill="#111" stroke="#fff" stroke-width="2"/><circle cx="94" cy="88" r="6" fill="#111" stroke="#fff" stroke-width="2"/></svg>
  We will come to you.</div>

<div class="abs services-band"></div>
<div class="abs thin-v" style="left:514px;top:1548px;height:30px"></div>
<div class="abs thin" style="left:482px;top:1574px;width:34px"></div>
<div class="abs thin-v" style="left:686px;top:1602px;height:28px"></div>
<div class="abs thin" style="left:686px;top:1602px;width:24px"></div>
<h2 class="abs section-title" style="top:1552px">Services</h2>
<div class="abs title-bar" style="top:1614px"></div>

<div class="abs tile tile-text" style="left:0;top:1663px;width:457px;height:278px;padding:28px 24px 0 160px">
  <p>We would really like it if the design somehow incorporates elements that highlight our unique selling points (repairs on location, we come to you etc.). We would really like some form of story telling in the design. Think clumsy people breaking their phones. Teenagers in tears because they have no access to their friends. People nowadays have the need to always be 'connected'. What happens when your phone is broken or malfunctioning? We're handling tech.</p>
  <p>we are nerds and a little bit weird, but we're professionals and here to help you with your problem. The sentiment Wire Troop tries to communicate is something we really like. We're looking for fresh idea's, anything goes!</p>
</div>
<div class="abs tile" style="left:457px;top:1663px;background:radial-gradient(ellipse 120px 90px at 150px 120px,#3f4a55,rgba(63,74,85,0)),radial-gradient(ellipse 90px 70px at 70px 220px,#b98f78,rgba(185,143,120,0)),linear-gradient(135deg,#e3e6ea,#a8b0b8 55%,#d4d8dc)" role="img" aria-label="Technician soldering a circuit board under a magnifier"></div>
<div class="abs tile" style="left:747px;top:1663px;background:radial-gradient(ellipse 130px 80px at 160px 150px,#d9b8a6,rgba(217,184,166,0)),radial-gradient(ellipse 110px 70px at 110px 110px,#6e747c,rgba(110,116,124,0)),linear-gradient(135deg,#c8ccd1,#eceae8 55%,#a9aeb4)" role="img" aria-label="Hands using a smartphone"></div>
<div class="abs tile" style="left:160px;top:1941px;width:297px;background:radial-gradient(ellipse 80px 110px at 220px 130px,#fafafa,rgba(250,250,250,0)),radial-gradient(ellipse 90px 70px at 80px 170px,#b9b9b6,rgba(185,185,182,0)),linear-gradient(135deg,#ebebe9,#d6d6d3 60%,#c4c4c1)" role="img" aria-label="Repair tools, gloves and a tablet laid out on a table"></div>
<div class="abs tile" style="left:457px;top:1941px;background:radial-gradient(ellipse 150px 90px at 200px 210px,#c9ae7c,rgba(201,174,124,0)),linear-gradient(135deg,#1f2730,#4f5d6a 50%,#8b8f86)" role="img" aria-label="Close-up of a gold phone with a cracked screen"></div>
<div class="abs tile" style="left:747px;top:1941px;background:radial-gradient(ellipse 90px 60px at 80px 200px,#7c8896,rgba(124,136,150,0)),radial-gradient(ellipse 110px 80px at 200px 110px,#ffffff,rgba(255,255,255,0)),linear-gradient(135deg,#f0f0f0,#dfe2e6 60%,#b7c0ca)" role="img" aria-label="Gloved hands repairing the inside of a phone"></div>
<div class="abs tile" style="left:160px;top:2219px;width:297px;height:275px;background:radial-gradient(ellipse 140px 100px at 190px 90px,#a9a9a9,rgba(169,169,169,0)),linear-gradient(135deg,#0b0b0b,#2c2c2c 55%,#6a6a6a)" role="img" aria-label="Shattered phone screen in dark light"></div>
<div class="abs tile" style="left:457px;top:2219px;height:275px;background:radial-gradient(ellipse 90px 90px at 190px 110px,#d7dde2,rgba(215,221,226,0)),radial-gradient(ellipse 110px 80px at 100px 220px,#f2f2f2,rgba(242,242,242,0)),linear-gradient(135deg,#aab2ba,#6c7680 55%,#c8ced3)" role="img" aria-label="Technician inspecting a phone with a magnifier"></div>
<div class="abs tile tile-text" style="left:747px;top:2219px;width:453px;height:275px;padding:26px 160px 0 16px">
  <p style="text-transform:uppercase;font-size:11.5px;line-height:1.5">In an overview all unique selling points of the Gadget haven service:</p>
  <ul>
    <li>- Professional service on location. Don't ship to us we will come to you!</li>
    <li>- Clear pricing upfront. No hidden cost.</li>
    <li>- Next business-day repair.</li>
    <li>- Backed by a professional call center open 12 hours a day and open on a Saturday as well</li>
    <li>- Backed by a professional repair center with more then 12 years of experience</li>
    <li>- Repair is done by certified engineers</li>
    <li>- 1 year warranty on the repair</li>
  </ul>
</div>

<section class="abs contact" role="img" aria-label="Dark close-up of a hand over a circuit board behind the contact form"></section>
<h2 class="abs contact-title">CONTACT US</h2>
<div class="abs field" style="left:278px;top:2706px;width:311px;height:41px">Your Name <b>*</b></div>
<div class="abs field" style="left:611px;top:2706px;width:311px;height:41px">Your Email <b>*</b></div>
<div class="abs field" style="left:278px;top:2766px;width:644px;height:150px">Your Message <b>*</b></div>
<div class="abs send">SEND MESSAGE</div>

<footer class="abs footer">
  <nav><a href="#">Home</a><a href="#">Who are we?</a><a href="#">Service</a><a href="#">The process</a><a href="#">Contact</a></nav>
  <small>© 2017 gadgethaven.com. All right reserved</small>
</footer>

</body>
</html>
```